Oaths and Harbors (Book cover needed)

Oaths and Harbors: Notes from a Career in Civic Work

Author: Perla Winthrop Okonedo

Foreword by Ambassador Delphine R. Osei

Book Trim Size: 5.5 x 8.5

```html
<!DOCTYPE html>
<html lang="en">
<head>
<meta charset="utf-8">
<title>Oaths and Harbors — Book Cover</title>
<link rel="stylesheet" href="https://fonts.googleapis.com/css2?family=Bebas+Neue&family=Montserrat:wght@600;700&display=swap">
<style>
  :root {
    --stage: #4a4a4a;
    --paper-light: #e6e6e6;
    --paper-mid: #d6d6d6;
    --gold: #c4902a;
    --slate: #7a7a7a;
    --white: #ffffff;
    --photo-top: #c4c4c4;
    --photo-mid: #7c7c7c;
    --photo-low: #2c2c2c;
  }
  * { margin: 0; padding: 0; box-sizing: border-box; }
  html, body {
    width: 1200px;
    height: 1200px;
    overflow: hidden;
    background: var(--stage);
  }
  .cover {
    position: absolute;
    left: 237px;
    top: 40px;
    width: 725px;
    height: 1120px;
    overflow: hidden;
    background: radial-gradient(ellipse at 40% 30%, var(--paper-light), var(--paper-mid));
  }
  .cover__author {
    position: absolute;
    top: 76px;
    left: 0;
    width: 100%;
    text-align: center;
    font-family: "Montserrat", sans-serif;
    font-weight: 700;
    font-size: 22px;
    letter-spacing: 0.5px;
    color: var(--gold);
  }
  .cover__portrait {
    position: absolute;
    left: 89px;
    top: 135px;
    width: 545px;
    height: 985px;
    border-radius: 180px 180px 0 0;
    background: linear-gradient(to bottom, var(--photo-top) 0%, var(--photo-mid) 40%, var(--photo-mid) 72%, var(--photo-low) 84%, var(--photo-low) 100%);
  }
  .cover__title {
    position: absolute;
    top: 640px;
    left: 0;
    width: 100%;
    text-align: center;
    font-family: "Bebas Neue", sans-serif;
    color: var(--gold);
    line-height: 0.82;
  }
  .cover__title-word { display: block; font-size: 140px; }
  .cover__title-joiner { display: block; font-size: 42px; line-height: 0.9; margin: 4px 0 2px; }
  .cover__subtitle {
    position: absolute;
    top: 926px;
    left: 0;
    width: 100%;
    text-align: center;
    font-family: "Montserrat", sans-serif;
    font-weight: 700;
    font-size: 21px;
    letter-spacing: 0.3px;
    color: var(--slate);
  }
  .cover__foreword {
    position: absolute;
    top: 1050px;
    left: 0;
    width: 100%;
    text-align: center;
    font-family: "Montserrat", sans-serif;
    font-weight: 700;
    font-size: 11px;
    letter-spacing: 0.2px;
    color: var(--white);
  }
</style>
</head>
<body>
  <main class="cover">
    <p class="cover__author">PERLA WINTHROP OKONEDO</p>
    <div class="cover__portrait" role="img" aria-label="Black-and-white portrait photograph of the smiling author in a head wrap, blazer and jeans"></div>
    <h1 class="cover__title">
      <span class="cover__title-word">OATHS</span>
      <span class="cover__title-joiner">AND</span>
      <span class="cover__title-word">HARBORS:</span>
    </h1>
    <p class="cover__subtitle">NOTES FROM A CAREER IN CIVIC WORK</p>
    <p class="cover__foreword">FOREWORD BY AMBASSADOR DELPHINE R. OSEI</p>
  </main>
</body>
</html>
```